Enterprise IT illustration needs a twist and uniquness

The attached Powerpoint shows four conceptual houses that consist of 5 / 6 building blocks. We will build a lot of content around this concept and want a design that looks crisp, in line with our brand colors guideline and with logo/ copyright embedded. Each building blocks should have unique color aligned with brand guideline so that content can easily aligned with the specific building block (by color). Look for a clean, modern design with a twist. Need the files also in formats where I can change text if needed at a later point.

```html
<!DOCTYPE html>
<html lang="en">
<head>
<meta charset="utf-8">
<title>Five Building Blocks – House Concepts</title>
<link rel="stylesheet" href="https://fonts.googleapis.com/css2?family=Poppins:wght@400&display=swap">
<style>
  :root {
    --roof: #27E1F7;
    --alerting: #2B3480;
    --topology: #FDD73F;
    --learn: #FD3B5F;
    --dashboard: #231F20;
    --harvest: #F5A533;
    --paper: #FFFFFF;
  }
  html, body { margin: 0; padding: 0; overflow: hidden; background: var(--paper); }
  .canvas { width: 1200px; height: 1200px; position: relative; overflow: hidden; background: var(--paper); }
  .houses { width: 1200px; height: 1200px; display: block; }
  .houses text { font-family: 'Poppins', sans-serif; font-weight: 400; }
  .block { fill: none; stroke-width: 10; stroke-linejoin: miter; }
  .num { font-size: 58px; }
  .label { font-size: 28px; }
  .roof { stroke: var(--roof); } .roof-fill { fill: var(--roof); } .t-roof { fill: var(--roof); }
  .alerting { stroke: var(--alerting); } .alerting-fill { fill: var(--alerting); } .t-alerting { fill: var(--alerting); }
  .topology { stroke: var(--topology); } .topology-fill { fill: var(--topology); } .t-topology { fill: var(--topology); }
  .learn { stroke: var(--learn); } .t-learn { fill: var(--learn); }
  .dashboard { stroke: var(--dashboard); } .t-dashboard { fill: var(--dashboard); }
  .harvest { stroke: var(--harvest); } .harvest-fill { fill: var(--harvest); } .t-harvest { fill: var(--harvest); }
</style>
</head>
<body>
<div class="canvas">
<svg class="houses" viewBox="0 0 1920 1920" xmlns="http://www.w3.org/2000/svg">

  <!-- House A: straight blocks -->
  <g class="house house-a">
    <polygon class="block roof" points="617,113 313,338 920,338"/>
    <text class="num t-roof" x="505" y="305">5</text>
    <text class="label t-roof" x="552" y="296">Taking action</text>

    <rect class="block alerting" x="315" y="381" width="487" height="82"/>
    <text class="num t-alerting" x="355" y="442">4</text>
    <text class="label t-alerting" x="408" y="432">Business relevant alerting</text>

    <rect class="block topology" x="315" y="505" width="222" height="165"/>
    <text class="num t-topology" x="330" y="609">3</text>
    <text class="label t-topology" x="377" y="582">Topology</text>
    <text class="label t-topology" x="377" y="614">discovery</text>

    <rect class="block learn" x="579" y="505" width="223" height="165"/>
    <text class="num t-learn" x="603" y="607">2</text>
    <text class="label t-learn" x="654" y="583">Learn &amp;</text>
    <text class="label t-learn" x="654" y="615">Control</text>

    <rect class="block dashboard" x="843" y="381" width="70" height="289"/>
    <text class="label t-dashboard" transform="translate(888,535) rotate(-90)" text-anchor="middle">+Dashboard</text>

    <rect class="block harvest" x="315" y="713" width="598" height="87"/>
    <text class="num t-harvest" x="432" y="777">1</text>
    <text class="label t-harvest" x="477" y="767">Qualtiy Data Harvesting</text>
  </g>

  <!-- House B: tilted tops -->
  <g class="house house-b">
    <polygon class="block roof" points="1395,113 1095,351 1695,351"/>
    <polygon class="roof-fill" points="1395,108 1395,128 1105,346 1095,351"/>
    <text class="num t-roof" x="1279" y="318">5</text>
    <text class="label t-roof" x="1327" y="308">Taking action</text>

    <polygon class="block alerting" points="1097,402 1345,392 1583,402 1583,488 1097,488"/>
    <text class="num t-alerting" x="1135" y="468">4</text>
    <text class="label t-alerting" x="1190" y="458">Business relevant alerting</text>

    <polygon class="block topology" points="1097,538 1210,529 1325,538 1325,703 1097,703"/>
    <text class="num t-topology" x="1113" y="642">3</text>
    <text class="label t-topology" x="1161" y="614">Topology</text>
    <text class="label t-topology" x="1161" y="647">discovery</text>

    <polygon class="block learn" points="1362,540 1583,540 1583,703 1362,703 1354,620"/>
    <text class="num t-learn" x="1386" y="640">2</text>
    <text class="label t-learn" x="1438" y="615">Learn &amp;</text>
    <text class="label t-learn" x="1438" y="648">Control</text>

    <rect class="block dashboard" x="1622" y="401" width="73" height="303"/>
    <text class="label t-dashboard" transform="translate(1668,553) rotate(-90)" text-anchor="middle">+Dashboard</text>

    <polygon class="block harvest" points="1097,755 1555,745 1693,754 1693,840 1097,840"/>
    <text class="num t-harvest" x="1207" y="816">1</text>
    <text class="label t-harvest" x="1253" y="806">Qualtiy Data Harvesting</text>
  </g>

  <!-- House C: tilted tops, lighter roof -->
  <g class="house house-c">
    <polygon class="block roof" points="602,903 300,1128 903,1128"/>
    <text class="num t-roof" x="485" y="1094">5</text>
    <text class="label t-roof" x="534" y="1084">Taking action</text>

    <polygon class="block alerting" points="304,1179 553,1169 795,1179 795,1265 304,1265"/>
    <text class="num t-alerting" x="345" y="1245">4</text>
    <text class="label t-alerting" x="400" y="1235">Business relevant alerting</text>

    <polygon class="block topology" points="304,1314 418,1306 531,1314 531,1478 304,1478"/>
    <text class="num t-topology" x="318" y="1418">3</text>
    <text class="label t-topology" x="367" y="1389">Topology</text>
    <text class="label t-topology" x="367" y="1422">discovery</text>

    <polygon class="block learn" points="574,1317 795,1317 795,1478 574,1478 567,1400"/>
    <text class="num t-learn" x="588" y="1417">2</text>
    <text class="label t-learn" x="640" y="1391">Learn &amp;</text>
    <text class="label t-learn" x="640" y="1424">Control</text>

    <rect class="block dashboard" x="829" y="1169" width="73" height="310"/>
    <text class="label t-dashboard" transform="translate(874,1325) rotate(-90)" text-anchor="middle">+Dashboard</text>

    <polygon class="block harvest" points="304,1532 760,1522 901,1530 901,1615 304,1615"/>
    <text class="num t-harvest" x="413" y="1592">1</text>
    <text class="label t-harvest" x="460" y="1582">Qualtiy Data Harvesting</text>
  </g>

  <!-- House D: tilted tops, heavier strokes -->
  <g class="house house-d">
    <polygon class="block roof" points="1380,903 1070,1140 1690,1140"/>
    <polygon class="roof-fill" points="1380,898 1380,922 1082,1136 1070,1140"/>
    <text class="num t-roof" x="1263" y="1094">5</text>
    <text class="label t-roof" x="1311" y="1084">Taking action</text>

    <polygon class="block alerting" points="1077,1185 1566,1185 1566,1278 1077,1278"/>
    <polygon class="alerting-fill" points="1077,1185 1566,1185 1566,1198 1325,1188 1077,1198"/>
    <text class="num t-alerting" x="1117" y="1257">4</text>
    <text class="label t-alerting" x="1172" y="1247">Business relevant alerting</text>

    <polygon class="block topology" points="1077,1324 1300,1324 1300,1495 1077,1495"/>
    <polygon class="topology-fill" points="1077,1324 1300,1324 1300,1338 1188,1330 1077,1340"/>
    <text class="num t-topology" x="1093" y="1434">3</text>
    <text class="label t-topology" x="1140" y="1405">Topology</text>
    <text class="label t-topology" x="1140" y="1438">discovery</text>

    <polygon class="block learn" points="1345,1324 1566,1324 1566,1495 1352,1495 1345,1410"/>
    <text class="num t-learn" x="1373" y="1431">2</text>
    <text class="label t-learn" x="1424" y="1404">Learn &amp;</text>
    <text class="label t-learn" x="1424" y="1437">Control</text>

    <rect class="block dashboard" x="1611" y="1184" width="72" height="312"/>
    <text class="label t-dashboard" transform="translate(1657,1340) rotate(-90)" text-anchor="middle">+Dashboard</text>

    <polygon class="block harvest" points="1077,1540 1682,1540 1682,1633 1077,1633"/>
    <polygon class="harvest-fill" points="1077,1540 1682,1540 1682,1554 1545,1546 1077,1554"/>
    <text class="num t-harvest" x="1192" y="1613">1</text>
    <text class="label t-harvest" x="1238" y="1603">Qualtiy Data Harvesting</text>
  </g>
</svg>
</div>
</body>
</html>
```